LANDING PAGE DESIGN - MONEY GUARANTEED & 2ND PLACE PAYOUT

brightlanework.net
Top Slide
Are you interested in earning from $65,000.00 - $91,000.00 a year from home?
NO PREVIOUS MARKETING EXPERIENCE NEEDED
---- scene 2 of slide --- please provide nice graphical images along with the text on each slide --
We are looking for motivated individuals from “GEO IP” with to join our team.
Qualify below to earn $100.00 a day while u learn to make $$
---Please don’t forget to create both slides when u post your design ---
Who should apply?
Anyone from the age of 18-65 who has at least 6 months experience using Chatterloop and or Swapboard. There is no marketing experience necessary or required and no background checks will be ran. The only really requirements are a home computer and internet connection and the ability to follow simple directions.

__featured jobs section__ Please make this section feature the 2 current available positions we are hiring for
Available Positions – Chatterloop AD Specialist –
Enroll in an 8 week training class that pays you $500.00 per week.
Training takes about 30-60 minutes a day 5 days a week for 8 weeks. Make $100.00 a day during training, and $250.00 a day 5-7 days a week after training is complete.
What do we do?
Help small businesses sale products through social media channels like Chatterloop & Pictavo. Our customers primary focus on the health and beauty niche.
Swapboardz Post Specialist
Enroll in a 6 weeks training that pays you $25.00 per day. Earn $100.00 a day after successfully completing your training. Course requires 30 minutes per day at least 3 times per week.
What do we do?
We help local real estate brokers, insurance agents, and other small businesses grow their businesses through targeted classified ad posting all over the country.

How do you apply?

First you must fill out our short application.
(Create an iframe - Frame #1)
First Name, Last Name, Age, City, State, Zip, Phone, Email
(Frame #2)
Do you have a desktop or laptop computer?
Do you have 24/7 access to the internet?
Are you at least 18 years old?
Do you have Photo ID? (must match your Chatterloop name)
Are you ready to start making money immediately?
(end of frames)

Testimonials Section
Leave space/frame for 3 video testimonials

Get Paid Referring Friends (need someway to track / pay for referrals)
We will pay you $5.00 for every qualified friend that you refer to us. Fill out the application above to get more information on our referral program.

After they complete the application I would like them to be sent an email saying that they qualify for both positions but we don’t have training agents available until “random day 2-3 months ahead”
BUT YOU QUALIFY FOR OUR SECONDARY OFFER
Would you like to earn $100.00 today – and up to $150.00 a week while getting a jump start on your training? “they click yes or no” when they click yes – it would take them to another page which explains to them to download TeamViewer so we can run ads from their CL promoting our partners and we will pay them weekly for it.

Target Market(s)

Lower Income Users Looking to make $$ from home who have an active Chatterloop account as well as a home computer and high speed internet.

Industry/Entity Type

Marketing

Number of Pages Required

1 page

Requirements
Must have
• This is a landing page / lead capturing page - So please make sure that the site focuses on pushing the user to enter their contact details and submit our qualifier form.
Nice to have
• I've always like the more cartoony websites - but must still be clean/professional looking with proper use of the fold of the page and whitespaces.

```html
<!DOCTYPE html>
<html lang="en">
<head>
<meta charset="utf-8">
<title>Brightlane Work – Earn From Home</title>
<link href="https://fonts.googleapis.com/css2?family=Questrial&family=Open+Sans:wght@400;600;700&display=swap" rel="stylesheet">
<style>
:root{
  --blue:#1a86c8;
  --blue-dark:#0f6fae;
  --ink:#1d1d1d;
  --body:#444;
  --dark:#111;
  --band:#4a3f38;
  --paper:#f1f1f1;
  --line:#d9d9d9;
  --white:#fff;
}
*{box-sizing:border-box;margin:0;padding:0}
html,body{width:1200px;height:2344px;overflow:hidden}
body{position:relative;font-family:"Open Sans",Arial,sans-serif;color:var(--body);background:var(--white)}
.abs{position:absolute}
.heading{font-family:"Questrial","Century Gothic",sans-serif;font-weight:400;color:var(--ink)}
.heading em{font-style:normal;color:var(--blue)}
.btn{position:absolute;display:flex;align-items:center;justify-content:center;font-size:14px;font-weight:600;letter-spacing:.5px;color:var(--white);text-transform:uppercase}
.btn-blue{background:var(--blue)}
.btn-black{background:var(--dark)}

/* header */
.site-header{left:0;top:0;width:1200px;height:114px;background:linear-gradient(#fff,#f3f3f3)}
.brand-name{left:164px;top:34px;font-family:"Questrial",sans-serif;font-size:38px;color:var(--blue);line-height:1}
.call{left:668px;top:76px;font-family:"Questrial",sans-serif;font-size:17px;color:#333}
.call b{font-weight:400;font-size:22px;color:var(--blue);margin-left:8px}

/* hero */
.hero{left:0;top:114px;width:1200px;height:492px;background:radial-gradient(ellipse at 50% 50%,#2493d3,var(--blue) 60%,#1478b8)}
.hero-title{left:164px;top:252px;width:460px;font-family:"Questrial",sans-serif;font-size:28px;line-height:39px;color:var(--white)}
.hero-sub{left:162px;top:374px;font-size:20px;font-weight:700;color:var(--white)}
.hero-art{left:640px;top:172px;width:454px;height:392px;border-radius:6px;background:linear-gradient(160deg,#e8eef2 0%,#3c6f86 55%,#1f3d4f 100%);opacity:.9}

/* who */
.who-art{left:156px;top:640px;width:134px;height:190px;border-radius:8px;background:linear-gradient(#f3d1a8,#2b2b2b)}
.who-rule{left:323px;top:640px;width:1px;height:190px;background:var(--line)}
.who-title{left:366px;top:656px;font-size:28px}
.mini-rule{height:1px;background:var(--line)}
.who-text{left:366px;top:730px;width:676px;font-size:12.5px;line-height:29px;color:#555}

/* featured */
.featured{left:0;top:880px;width:1200px;height:507px;background:linear-gradient(100deg,#5b4c41,var(--band) 45%,#3b342f)}
.feat-title{left:0;top:926px;width:1200px;text-align:center;font-size:27px;color:var(--white)}
.job{color:#eee;font-size:12px;line-height:23px}
.job h3{font-family:"Questrial",sans-serif;font-weight:400;font-size:17px;color:var(--white);margin-bottom:10px}
.job h4{font-family:"Questrial",sans-serif;font-weight:400;font-size:17px;color:var(--white);margin:14px 0 4px}
.job p{margin-bottom:8px}
.job .divider{height:1px;background:rgba(255,255,255,.25);margin:6px 0 12px}
.job-left{left:75px;top:1014px;width:336px;text-align:right}
.job-right{left:794px;top:1014px;width:300px}
.job-icon{width:38px;height:38px;border-radius:50%;border:2px solid var(--white)}
.feat-art{left:478px;top:1062px;width:252px;height:200px;border-radius:6px;background:linear-gradient(#d9b98f 0%,#8fb54a 35%,#ffffff 60%,#c9c9c9 100%);opacity:.9}

/* apply */
.apply{left:0;top:1387px;width:1200px;height:449px;background:var(--paper)}
.apply-title{left:0;top:1430px;width:1200px;text-align:center;font-size:28px}
.apply-lead{left:0;top:1503px;width:1200px;text-align:center;font-size:13px;color:#333}
.field{position:absolute;width:206px;height:34px;background:var(--white);border:1px solid #ddd;font-size:12px;color:#777;padding:9px 16px}
.check{position:absolute;left:650px;display:flex;align-items:center;gap:10px;font-size:12.5px;color:var(--blue)}
.box{width:12px;height:12px;border:1px solid #777;background:var(--white)}

/* testimonials */
.say-title{left:0;top:1880px;width:1200px;text-align:center;font-size:28px}
.video{position:absolute;top:1961px;width:273px;height:188px;border:4px solid #e5e5e5}
.video-fill{position:absolute;inset:0}
.play{position:absolute;left:50%;top:50%;width:36px;height:36px;margin:-28px 0 0 -18px;border-radius:50%;background:rgba(255,255,255,.5)}
.play::after{content:"";position:absolute;left:14px;top:10px;border-left:11px solid #fff;border-top:8px solid transparent;border-bottom:8px solid transparent}
.video-cap{position:absolute;right:14px;bottom:8px;font-size:14px;font-weight:600;color:var(--white)}
.refer-title{left:0;top:2174px;width:1200px;text-align:center;font-size:16px;color:var(--blue)}
.refer-text{left:300px;top:2204px;width:600px;text-align:center;font-size:12px;line-height:22px;color:#444}

/* footer */
.site-footer{left:0;top:2297px;width:1200px;height:47px;background:var(--dark)}
.copy{left:164px;top:2313px;font-size:12px;color:#ddd}
.social{top:2308px;width:24px;height:24px;border-radius:50%;background:var(--blue);border:2px solid #fff}
</style>
</head>
<body>

<header class="site-header abs">
  <div class="brand-name abs">Brightlane Work</div>
  <a class="btn btn-black" style="left:773px;top:19px;width:157px;height:36px">
    <svg width="14" height="14" viewBox="0 0 14 14" style="margin-right:8px"><path d="M2 12l1-4 7-7 3 3-7 7z" fill="#fff"/></svg>Sign up now</a>
  <a class="btn btn-blue" style="left:939px;top:19px;width:99px;height:36px">
    <svg width="12" height="14" viewBox="0 0 12 14" style="margin-right:8px"><circle cx="6" cy="4" r="3.5" fill="#fff"/><path d="M0 14c0-5 12-5 12 0z" fill="#fff"/></svg>Login</a>
  <div class="call abs">Have a question? Call Us Now <b>555 014 2290</b></div>
</header>

<section class="hero abs">
  <svg class="abs" style="left:64px;top:204px" width="40" height="80" viewBox="0 0 40 80"><path d="M38 2L2 40l36 38" fill="none" stroke="#fff" stroke-width="2"/></svg>
  <svg class="abs" style="left:1096px;top:204px" width="40" height="80" viewBox="0 0 40 80"><path d="M2 2l36 38L2 78" fill="none" stroke="#fff" stroke-width="2"/></svg>
</section>
<h1 class="hero-title abs">Are You Interested In Earning From $65,000.00 - &nbsp;$91,000.00 A Year From Home?</h1>
<p class="hero-sub abs">No Previous Marketing Experience Needed</p>
<a class="btn btn-black" style="left:162px;top:422px;width:158px;height:36px">Contact now</a>
<div class="hero-art abs" role="img" aria-label="Cartoon man working at a computer desk with a cat and plant"></div>

<section>
  <div class="who-art abs" role="img" aria-label="Cartoon businessman in a suit pointing to the text"></div>
  <div class="who-rule abs"></div>
  <h2 class="who-title heading abs">Who <em>should apply</em></h2>
  <div class="mini-rule abs" style="left:366px;top:710px;width:620px"></div>
  <p class="who-text abs">Anyone from the age of 18-65 who has at least 6 months experience using Chatterloop and or Swapboard. There is no marketing experience necessary or required and no background checks will be ran. The only really requirements are a home computer and internet connection and the ability to follow simple directions.</p>
</section>

<section class="featured abs"></section>
<h2 class="feat-title heading abs" style="color:#fff">Featured Jobs</h2>
<div class="abs" style="left:443px;top:978px;width:314px;height:1px;background:rgba(255,255,255,.35)"></div>
<div class="job-icon abs" style="left:433px;top:1012px;background:#2f5aa8"></div>
<div class="job-icon abs" style="left:734px;top:1012px;background:#5b3a9e"></div>
<svg class="abs" style="left:496px;top:1016px" width="52" height="24" viewBox="0 0 52 24"><path d="M50 20C40 6 20 4 4 10m0 0l8-7m-8 7l9 5" fill="none" stroke="#fff" stroke-width="2"/></svg>
<svg class="abs" style="left:660px;top:1016px" width="52" height="24" viewBox="0 0 52 24"><path d="M2 20C12 6 32 4 48 10m0 0l-8-7m8 7l-9 5" fill="none" stroke="#fff" stroke-width="2"/></svg>
<div class="feat-art abs" role="img" aria-label="Cartoon man with laptop sitting at a desk with folders"></div>

<article class="job job-left abs">
  <h3>Chatterloop AD Specialist</h3>
  <p>Enroll in an <b>8 week training</b> class that pays you <b>$500.00</b> per week.</p>
  <p>Training takes about 30-60 minutes a day 5 days a week for 8 weeks. Make $100.00 a day during training, and $250.00 a day 5-7 days a week after training is complete.</p>
  <div class="divider"></div>
  <h4>What do we do?</h4>
  <p>Help small businesses sale products through social media channels like Chatterloop &amp; Pictavo. Our customers primary focus on the health and beauty niche.</p>
</article>
<article class="job job-right abs">
  <h3>Swapboardz Post Specialist</h3>
  <p>Enroll in a <b>6 weeks</b> training that pays you <b>$25.00</b> per day.</p>
  <p><b>Earn $100.00</b> a day after successfully completing your training. Course requires 30 minutes per day at least 3 times per week.</p>
  <div class="divider"></div>
  <h4>What do we do?</h4>
  <p>We help local real estate brokers, insurance agents, and other small businesses grow their businesses through targeted classified ad posting all over the country.</p>
</article>
<a class="btn btn-blue" style="left:523px;top:1300px;width:152px;height:36px">Contact now</a>

<section class="apply abs"></section>
<h2 class="apply-title heading abs">How do <em>you apply?</em></h2>
<div class="mini-rule abs" style="left:450px;top:1482px;width:300px"></div>
<p class="apply-lead abs">First you must fill out our short application.</p>
<form>
  <div class="field" style="left:200px;top:1555px">First Name</div>
  <div class="field" style="left:416px;top:1555px">Last Name</div>
  <div class="field" style="left:200px;top:1598px">Age</div>
  <div class="field" style="left:416px;top:1598px">City</div>
  <div class="field" style="left:200px;top:1642px">State</div>
  <div class="field" style="left:416px;top:1642px">Zip</div>
  <div class="field" style="left:200px;top:1687px">Phone</div>
  <div class="field" style="left:416px;top:1687px">Email</div>
  <div class="check" style="top:1554px"><span class="box"></span>Do you have a desktop or laptop computer?</div>
  <div class="check" style="top:1592px"><span class="box"></span>Do you have 24/7 access to the internet?</div>
  <div class="check" style="top:1631px"><svg class="box" viewBox="0 0 12 12"><path d="M2 6l3 3 6-7" fill="none" stroke="#333" stroke-width="1.6"/></svg>Are you at least 18 years old?</div>
  <div class="check" style="top:1669px"><svg class="box" viewBox="0 0 12 12"><path d="M2 6l3 3 6-7" fill="none" stroke="#333" stroke-width="1.6"/></svg>Do you have Photo ID? (must match your Chatterloop name)</div>
  <div class="check" style="top:1708px"><svg class="box" viewBox="0 0 12 12"><path d="M2 6l3 3 6-7" fill="none" stroke="#333" stroke-width="1.6"/></svg>Are you ready to start making money immediately?</div>
  <a class="btn btn-blue" style="left:523px;top:1745px;width:152px;height:36px">Submit now</a>
</form>

<section>
  <h2 class="say-title heading abs">What People <em>Are Saying</em></h2>
  <div class="mini-rule abs" style="left:450px;top:1929px;width:300px"></div>
  <div class="video" style="left:162px">
    <div class="video-fill" role="img" aria-label="Video testimonial from a smiling older woman" style="background:linear-gradient(120deg,#e9e2d6,#b9a892)"></div>
    <span class="play"></span><span class="video-cap">Lorem Ipsum dolor</span>
  </div>
  <div class="video" style="left:464px">
    <div class="video-fill" role="img" aria-label="Video testimonial from a man in a suit in an office" style="background:linear-gradient(120deg,#d8c7a6,#5b4b3c)"></div>
    <span class="play"></span><span class="video-cap">Lorem Ipsum dolor</span>
  </div>
  <div class="video" style="left:766px">
    <div class="video-fill" role="img" aria-label="Video testimonial from a man in a plaid shirt at home" style="background:linear-gradient(120deg,#d9d4c8,#4a6a9a)"></div>
    <span class="play"></span><span class="video-cap">Lorem Ipsum dolor</span>
  </div>
  <h3 class="refer-title heading abs" style="color:var(--blue)">Get Paid Referring Friends (need someway to track / pay for referrals)</h3>
  <p class="refer-text abs">We will pay you $5.00 for every qualified friend that you refer to us. Fill out the application above to get more information on our referral program.</p>
</section>

<footer class="site-footer abs"></footer>
<p class="copy abs">Copyright ©2017 Brightlane LP. All Rights Reserved.</p>
<span class="social abs" style="left:924px"></span>
<span class="social abs" style="left:954px"></span>
<span class="social abs" style="left:984px"></span>
<span class="social abs" style="left:1014px;background:#f39c12"></span>

</body>
</html>
```